Business Card for Brightvale Homestead Care

I need a business card design for a very elite and personalized companion care company. We take care of the client at home with respect, dignity, and our full attention. The design should communicate a classic elegance and trust.

```html
<!DOCTYPE html>
<html lang="en">
<head>
<meta charset="utf-8">
<title>Brightvale Homestead Care – Business Card</title>
<link href="https://fonts.googleapis.com/css2?family=Arimo:wght@400;700&display=swap" rel="stylesheet">
<style>
  :root {
    --backdrop: #0c0c0d;
    --card: #2a2a2c;
    --card-edge: #1577b8;
    --brand-blue: #1a6fb0;
    --accent-blue: #22a6e0;
    --text-grey: #c9c9cc;
    --rule: #47474b;
  }
  * { margin: 0; padding: 0; box-sizing: border-box; }
  html, body {
    width: 1200px; height: 822px; overflow: hidden;
    background: var(--backdrop);
    font-family: "Arimo", Arial, sans-serif;
  }
  .stage {
    width: 1200px; height: 822px;
    display: flex; align-items: center; justify-content: center; gap: 60px;
  }
  .card {
    position: relative;
    width: 520px; height: 297px;
    background: var(--card);
    border-bottom: 3px solid var(--card-edge);
    border-left: 1px solid var(--card-edge);
    box-shadow: 0 18px 40px rgba(0,0,0,.6);
  }
  .brand {
    position: absolute; right: 34px; top: 44px;
    display: flex; align-items: center; gap: 8px;
    color: var(--brand-blue);
    font-size: 21px; font-weight: 400; letter-spacing: .5px;
  }
  .brand-dot {
    width: 9px; height: 9px; border-radius: 50%;
    background: var(--accent-blue);
  }
  .card-back .brand { top: 50%; transform: translateY(-50%); }
  .divider {
    position: absolute; left: 34px; right: 34px; top: 112px;
    height: 1px; background: var(--rule);
  }
  .person { position: absolute; left: 34px; top: 140px; }
  .person-name {
    color: var(--brand-blue); font-weight: 700; font-size: 17px;
    text-transform: uppercase; letter-spacing: .3px;
  }
  .person-role { color: var(--text-grey); font-size: 13px; margin-top: 3px; }
  .contacts { position: absolute; left: 34px; bottom: 30px; list-style: none; }
  .contacts li {
    display: flex; align-items: center; gap: 8px;
    color: var(--text-grey); font-size: 13px; line-height: 20px;
  }
  .contacts svg { width: 13px; height: 13px; flex: none; }
  .address {
    position: absolute; right: 34px; top: 140px;
    text-align: right; color: var(--text-grey); font-size: 13px; line-height: 18px;
  }
</style>
</head>
<body>
<main class="stage">
  <section class="card card-front">
    <div class="brand"><span class="brand-dot"></span>Brightvale Homestead Care</div>
    <div class="divider"></div>
    <div class="person">
      <p class="person-name">Daniel Whitmore</p>
      <p class="person-role">Managing Director</p>
    </div>
    <address class="address">88, Linden Row Lane<br>Harwick County, 30217</address>
    <ul class="contacts">
      <li>
        <svg viewBox="0 0 14 14"><rect x="0.5" y="0.5" width="13" height="13" rx="2" fill="none" stroke="#1a6fb0"/><path d="M4 3.5l1.5 0 .8 2-1 .8a5 5 0 0 0 2.4 2.4l.8-1 2 .8v1.5c0 .4-.4.8-.8.8A7 7 0 0 1 3.2 4.3c0-.4.4-.8.8-.8z" fill="#1a6fb0"/></svg>
        044-555 018 273
      </li>
      <li>
        <svg viewBox="0 0 14 14"><rect x="0.5" y="2.5" width="13" height="9" fill="#1a6fb0"/><path d="M1 3l6 5 6-5" fill="none" stroke="#2a2a2c" stroke-width="1.2"/></svg>
        hello@brightvalehome.com
      </li>
      <li>
        <svg viewBox="0 0 14 14"><circle cx="7" cy="7" r="6.3" fill="#1a6fb0"/><path d="M.7 7h12.6M7 .7c-3 3.5-3 9 0 12.6M7 .7c3 3.5 3 9 0 12.6" fill="none" stroke="#2a2a2c" stroke-width=".9"/></svg>
        www.brightvalehome.com
      </li>
    </ul>
  </section>

  <section class="card card-back">
    <div class="brand"><span class="brand-dot"></span>Brightvale Homestead Care</div>
  </section>
</main>
</body>
</html>
```